Riverbend Haven Home Care-Nursing Assessment Form

I am creating a Nursing Assessment Form (which is used to be an intake form for all new patients) for my new home care company, Riverbend Haven Home Care.

It is 15 pages and pretty comprehensive as this is a very regulated field. I have all the necessary content and information attached in the word document below. Now, I am seeking a designer to make it look professional, cohesive and easy to read/ follow.
In order for your Word Document Design to be selected, you must:

1. As mentioned previously, make it easy to read/follow. There should be enough spacing, room to write out all necessary notes, fill out check marks...etc...
2. It should look professional.
3. It should be attractive and eye pleasing. Attached you will find our logo-kindly incorporate it's style into the project as well. The logo should be placed on top of each page.
4. Lastly, we need a Word Document version AND PDF Fillable Option. The fillable PDF should Auto Fill for the Name and Start of Care (SOC) Date.

I have attached a sample form below as well. This is how I envision the finished project to look. Of course, I am open to other suggestions as look as it meets the aforementioned requirements.

Thank you! May the best man or woman win!
Our team looks forward to working with our designer on this project!

Industry/Entity Type

Home Health Care

Font styles to use
Sans Serif

Colors
0255a3
9bcb3c

Requirements
Must have
• Refer to Project Description above.
Nice to have
We must be given a Word Document Option and PDF Fillable Option.

```html
<!DOCTYPE html>
<html lang="en">
<head>
<meta charset="utf-8">
<title>Riverbend Haven Home Care – Initial Assessment Form</title>
<link rel="stylesheet" href="https://fonts.googleapis.com/css2?family=Roboto+Condensed:ital,wght@0,400;0,700;1,400&display=swap">
<style>
  :root{
    --blue:#0255a3;
    --ink:#243a6b;
    --green:#9bcb3c;
    --green-mid:#b8d97a;
    --green-soft:#c9e2a0;
    --tint:#f1f7e6;
    --rule:#aebbd6;
    --bg:#e8e9eb;
  }
  *{box-sizing:border-box;margin:0;padding:0}
  html,body{width:1200px;height:1200px;overflow:hidden}
  body{background:var(--bg);font-family:"Roboto Condensed",Arial,sans-serif;color:var(--ink);position:relative}
  .page{position:absolute;top:249px;width:497px;height:702px;background:#fff;box-shadow:0 6px 14px rgba(0,0,0,.28)}
  .page-left{left:59px}
  .page-right{left:643px}
  .wave{position:absolute;top:0;left:0;width:497px;height:72px}
  .brand{position:absolute;left:29px;top:58px;display:flex;align-items:center;gap:5px}
  .brand-dot{width:10px;height:10px;border-radius:50%;background:var(--green)}
  .brand-name{font-size:9.5px;font-weight:700;color:var(--blue);text-transform:uppercase;letter-spacing:.2px}
  .title{position:absolute;right:30px;top:74px;font-size:15px;font-weight:700;color:var(--blue)}
  .body{position:absolute;left:29px;right:29px;top:112px;font-size:7.6px}
  .row{display:flex;align-items:flex-end;height:13px;padding:0 4px 1.5px;border-bottom:.8px solid var(--rule);white-space:nowrap}
  .row.plain{border-bottom:none}
  .row.center{justify-content:center}
  .row.tall{height:auto;align-items:flex-start;padding-top:2px}
  .row span{display:inline-block}
  .name-row{padding:0;border:none;margin-bottom:15px}
  .name-row .line{flex:1;border-bottom:.8px solid var(--ink);margin:0 2px 2px}
  .shade{background:var(--tint)}
  .gap{height:7px}
  .bar{height:12px;margin:0 -2px 1px;border-radius:4px;background:var(--green-soft);color:var(--blue);font-weight:700;font-size:7.6px;text-align:center;line-height:12px;text-transform:uppercase}
  .bar.empty{background:var(--green-soft)}
  .checks{display:grid;grid-template-columns:105px 177px 1fr;padding:3px 4px 0;row-gap:0}
  .checks span{height:13px;line-height:13px}
  .ability{display:grid;grid-template-columns:120px 135px 1fr;padding:2px 4px 0}
  .ability span{line-height:9.5px;margin-bottom:3px}
  .cb{display:inline-block;width:7px;height:7px;border:.8px solid #6e7380;margin:0 2px 0 5px;vertical-align:-1px}
  .abuse{background:var(--tint);height:46px;margin-bottom:10px}
  .abuse .row{border:none}
  .abuse .row.ruled{border-bottom:.8px solid var(--ink)}
  .nutri{display:flex;justify-content:space-between;margin-top:7px;height:156px}
  .nutri-table{width:288px;font-size:5.4px}
  .nt-head{display:flex;background:var(--green-soft);height:9px;line-height:9px;font-style:italic}
  .nt-head .st{flex:1;text-align:center}
  .nt-head .val{width:24px;text-align:center;background:var(--green-mid)}
  .nt-row{display:flex;align-items:center;height:13.5px}
  .nt-row .st{flex:1;padding-left:4px}
  .nt-row .st::before{content:"•";margin-right:12px}
  .nt-row .box{width:24px;height:10px;border:.8px solid var(--green-soft)}
  .nt-total{display:flex;justify-content:flex-end;align-items:center;height:12px;font-weight:700}
  .nt-total .box{width:24px;height:10px;border:.8px solid var(--green-soft);margin-left:5px}
  .nutri-key{width:134px;height:142px;background:var(--green-mid);border-radius:4px;padding:12px 8px;font-size:6.2px;font-style:italic;line-height:8.5px;color:var(--ink)}
  .nutri-key p{margin-bottom:9px}
  .nutri-key b{font-style:normal}
  .spread{justify-content:space-around}
</style>
</head>
<body>

<section class="page page-left">
  <svg class="wave" viewBox="0 0 497 72" preserveAspectRatio="none" aria-hidden="true">
    <path d="M0 0H497V52C420 28 330 12 250 16C160 20 80 40 0 32Z" fill="#c9e2a0"/>
    <path d="M0 0H470C400 6 320 30 230 46C180 55 120 60 0 52Z" fill="#9bcb3c" opacity=".55"/>
    <path d="M0 0H400C330 8 240 20 150 22C90 24 40 26 0 32Z" fill="#8cc63f"/>
  </svg>
  <div class="brand"><span class="brand-dot"></span><span class="brand-name">Riverbend Haven Home Care</span></div>
  <h1 class="title">Initial Assessment Form</h1>

  <div class="body">
    <div class="row name-row"><span>Name</span><span class="line" style="flex:0 0 170px"></span><span style="margin-left:auto">SOC Date:</span><span class="line" style="flex:0 0 102px"></span></div>

    <div class="shade">
      <div class="row"><span style="width:243px">Patient's Name:</span><span style="width:67px">Gender:</span><span style="width:58px">MR#:</span><span>Date:</span></div>
      <div class="row"><span style="width:243px">Primary Diagnosis:</span><span>Secondary Diagnosis:</span></div>
      <div class="row"><span style="width:243px">Other Pertinent Diagnosis:</span><span>PCP name:</span></div>
      <div class="row"><span>Other Physician Name:</span></div>
    </div>
    <div class="gap"></div>
    <div class="row plain"><span style="width:47px">Prognosis:</span><span style="width:65px">( ) Poor</span><span style="width:65px">( ) Fair</span><span style="width:65px">(&nbsp; ) Good</span><span>( ) Excellent</span></div>
    <div class="row"><span style="width:47px">Vital Signs:</span><span style="width:65px">Height:</span><span style="width:65px">Weight:</span><span style="width:65px">Temp:</span><span style="width:65px">Pulse:</span><span style="width:62px">Resp:</span><span>B/P:</span></div>
    <div class="row"><span>Allergies:</span></div>
    <div class="row" style="height:16px"><span>Past Medical and Surgical History:</span></div>
    <div class="row"></div>
    <div class="gap"></div>

    <div class="bar">Support Systems</div>
    <div class="row plain center"><span>Married/Not Married/Single/Divorced/Widowed</span></div>
    <div class="row plain"><span>Lives Alone:&nbsp; ( ) Yes&nbsp;&nbsp; ( ) No</span></div>
    <div class="row"><span>Family Composition:</span></div>
    <div class="row"><span>Past Medical and Surgical History:</span></div>
    <div class="row"><span style="width:307px">Legal Next of Kin:</span><span>Telephone:</span></div>
    <div class="row"><span style="width:307px">Address:</span><span>E-mail:</span></div>
    <div class="row plain"><span>Is significant other able, available, capable and willing to care for patient?&nbsp; ( ) Yes&nbsp;&nbsp; ( ) No</span></div>
    <div class="row"><span>If No, explain:</span></div>
    <div class="row"><span>Educational Needs of Patient/Family:</span></div>
    <div class="gap"></div>

    <div class="bar">Environment</div>
    <div class="row plain center"><span style="margin-right:20px">( ) Private Home</span><span style="margin-right:20px">( ) Apartment</span><span style="margin-right:20px">( ) Elevator</span><span>( ) Walkup</span></div>
    <div class="gap"></div>
    <div class="bar empty"></div>
    <div class="checks">
      <span>( ) Sound structure</span><span>( ) Safe Placement of Cords, Rugs and Furniture</span><span>( ) Adequate Heating and Ventilation</span>
      <span>( ) Adequate Cooking facility</span><span>( ) Adequate Plumbing/Sanitation/ Running Water</span><span>( ) Adequate Sleeping Arrangement</span>
      <span>( ) Infestations of pests?</span><span>( ) Safe Gas/Electric Appliances</span><span>( ) Enough Electrical Outlets for Equipment</span>
      <span>( ) Neighborhood safe?</span><span>( ) Safe storage for Supplies/Equipment/Meds?</span><span>( )&nbsp; Exits Free of Obstruction</span>
      <span>( ) Fire extinguisher in home?</span><span>( ) Grounded Plug for Equipment</span><span>( ) Working Telephone in the Home</span>
      <span>( ) Working smoke detectors?</span><span></span><span></span>
    </div>
    <div class="gap"></div>

    <div class="bar">Caregiver's Contact Information</div>
    <div class="row"><span style="width:242px">Name:</span><span style="width:112px">Telephone:</span><span>/</span></div>
    <div class="row"><span style="width:242px">Address:</span><span>Email:</span></div>
    <div class="row"><span>Days / Time Available:</span></div>
    <div class="gap"></div>

    <div class="bar" style="text-transform:none">Caregivers Ability to Assist Patient / Able to Provide</div>
    <div class="ability">
      <span>Personal Care: ( ) Yes ( ) No</span><span>Mobility: ( ) Yes ( ) No</span><span>Prepare/Serve Meals: ( ) Yes ( ) No</span>
      <span>Maintain Safe/Clean Environment:<br>( ) Yes ( ) No</span><span>Perform/ Assist with Procedures:<br>( ) Yes ( ) No</span><span>Caregiver has capacity to learn therapeutic regimen:<br>(&nbsp; ) Yes (&nbsp; ) No</span>
    </div>
    <div class="row plain"><span>Comments:</span></div>
    <div class="row"></div>
  </div>
</section>

<section class="page page-right">
  <svg class="wave" viewBox="0 0 497 72" preserveAspectRatio="none" aria-hidden="true">
    <path d="M0 0H497V52C420 28 330 12 250 16C160 20 80 40 0 32Z" fill="#c9e2a0"/>
    <path d="M0 0H470C400 6 320 30 230 46C180 55 120 60 0 52Z" fill="#9bcb3c" opacity=".55"/>
    <path d="M0 0H400C330 8 240 20 150 22C90 24 40 26 0 32Z" fill="#8cc63f"/>
  </svg>
  <div class="brand" style="top:54px"><span class="brand-dot"></span><span class="brand-name">Riverbend Haven Home Care</span></div>
  <h1 class="title" style="top:70px">Initial Assessment Form</h1>

  <div class="body" style="top:106px">
    <div class="row name-row" style="margin-bottom:6px"><span>Name</span><span class="line" style="flex:0 0 170px"></span><span style="margin-left:auto">SOC Date:</span><span class="line" style="flex:0 0 102px"></span></div>

    <div class="abuse">
      <div class="row"><span>Are There Any Signs of Abuse or Neglect from Family or Caregiver?:</span><span><span class="cb"></span>Yes<span class="cb"></span>No</span></div>
      <div class="row ruled"><span>If Yes, describe:</span></div>
    </div>

    <div class="bar">Advanced Directives</div>
    <div class="row plain" style="height:14px"><span style="width:197px">Patient has a Living Will <span class="cb"></span>Yes <span class="cb"></span>No</span><span>Health Care Proxy <span class="cb"></span>Yes <span class="cb"></span>No</span></div>
    <div class="row plain"><span style="width:100px">Special Provisions Included:</span><span><span class="cb"></span>DNR <span class="cb"></span>DNI <span class="cb"></span>No Mech. Ventilation <span class="cb"></span>Med. Support Only <span class="cb"></span>No Feeding Tubes</span></div>
    <div class="row plain"><span style="width:100px"></span><span><span class="cb"></span>Copies of Documentation Attached <span class="cb"></span>Yes <span class="cb"></span>No</span></div>
    <div class="row"><span>Other:</span></div>
    <div class="gap"></div>

    <div class="bar">Nutritional</div>
    <div class="row"><span style="width:197px">Diet:</span><span>Meals Prepared By:</span></div>
    <div class="row"><span>Meals Patterns/Tolerance/Restrictions:</span></div>
    <div class="row plain"><span>Compliance: <span class="cb"></span>Yes <span class="cb"></span>No</span></div>

    <div class="nutri">
      <div class="nutri-table">
        <div class="nt-head"><span class="st">Statement</span><span class="val">Value</span></div>
        <div class="nt-row"><span class="st">I have an illness or condition that made me change the kind and/or amount of food I eat</span><span class="box"></span></div>
        <div class="nt-row"><span class="st">I eat fewer than two meals per day</span><span class="box"></span></div>
        <div class="nt-row"><span class="st">I do not eat fruits, vegetables or milk products</span><span class="box"></span></div>
        <div class="nt-row"><span class="st">I have three of more drinks of beer, liquor or wine almost every day</span><span class="box"></span></div>
        <div class="nt-row"><span class="st">I have a tooth or mouth problems that make it hard for me to eat</span><span class="box"></span></div>
        <div class="nt-row"><span class="st">I don't always have enough money to buy food</span><span class="box"></span></div>
        <div class="nt-row"><span class="st">I eat alone most of the time</span><span class="box"></span></div>
        <div class="nt-row"><span class="st">I have three or more different prescribed drugs or over-the counter drugs per day</span><span class="box"></span></div>
        <div class="nt-row"><span class="st">Without wanting to, I have gained or lost ten pounds in the last six months</span><span class="box"></span></div>
        <div class="nt-row"><span class="st">I am not always physically able to shop, cook or feed myself</span><span class="box"></span></div>
        <div class="nt-total">TOTAL<span class="box"></span></div>
      </div>
      <div class="nutri-key">
        <p><b>0-2</b>: Low Nutritional Risks:<br>Continue to evaluate Patient's nutritional needs and intervene as needed.</p>
        <p><b>3-5</b>: Moderate Nutritional Risk:<br>Educate patient/family/caregiver and improve Patient's eating habits and lifestyle.</p>
        <p><b>6+</b>: High Nutritional Risk:<br>Notify MD for further orders if indicated and consider special diet.</p>
      </div>
    </div>

    <div class="bar">Exercise</div>
    <div class="row plain spread" style="height:15px"><span><span class="cb"></span>less than 1 hr week</span><span><span class="cb"></span>2-5 hr per week</span><span><span class="cb"></span>more than 6 hours per week</span></div>
    <div class="gap" style="height:5px"></div>

    <div class="bar">Immunizations/Screening Tests</div>
    <div class="row plain"><span style="width:221px">Immunizations: Flu <span class="cb"></span>Yes <span class="cb"></span>No&nbsp;&nbsp; Date:</span><span>Pneumonia <span class="cb"></span>Yes <span class="cb"></span>No&nbsp;&nbsp; Date:</span></div>
    <div class="row plain"><span style="width:221px">Screening: Cholesterol level <span class="cb"></span>Yes <span class="cb"></span>No&nbsp;&nbsp; Date:</span><span>Colon cancer screen <span class="cb"></span>Yes <span class="cb"></span>No&nbsp;&nbsp; Date:</span></div>
    <div class="row plain"><span style="width:221px">Mammogram <span class="cb"></span>Yes <span class="cb"></span>No&nbsp;&nbsp; Date:</span><span>Prostate cancer screen <span class="cb"></span>Yes <span class="cb"></span>No&nbsp;&nbsp; Date:</span></div>
    <div class="gap" style="height:5px"></div>

    <div class="bar">Activities of Daily Living</div>
    <div class="row plain tall" style="height:40px"><span style="width:130px">Need assistance in the following areas:</span><span style="white-space:normal;width:300px;line-height:10px"><span class="cb"></span>Bathing/Showering <span class="cb"></span>Toileting <span class="cb"></span>Ambulation <span class="cb"></span>Dressing <span class="cb"></span>Transfers<br><span class="cb"></span>Eating/Meal preparation <span class="cb"></span>Medication Reminders <span class="cb"></span>Shopping <span class="cb"></span>Housekeeping<br><span class="cb"></span>Laundry</span></div>
    <div class="row"><span><span class="cb" style="margin-left:2px"></span>Other:</span></div>
  </div>
</section>

</body>
</html>
```